Commercial Broker Profile Flyer

I need a one-page flyer created that will serve as a profile report for individual brokers within a commercial real estate firm. The flyer will include company branding, agent photo, bio, and other information. I would like to have the source file available for future editing preferably in a Publisher file format. A copy of a company brochure is included and would like to have this profile flyer similar to keep company branding consistent. Our company website is www.holbrookvalere.com for any other questions on branding.
Updates

Target Market(s)

Professional

Industry/Entity Type

Real Estate Agent

Requirements
Must have
• One page
• Source files MUST include a .PUB file that I can update in the future
• All of the information in the uploaded "content" file
• Company branding
• Must be 8.5"x11"
Should not have
• Do not use stock photos or property photos from the attachments. I only want the broker photo and company logo.

```html
<!DOCTYPE html>
<html lang="en">
<head>
<meta charset="utf-8">
<title>Broker Profile Flyer – Holbrook Valere Real Estate</title>
<link href="https://fonts.googleapis.com/css2?family=Lato:wght@400;700&family=Oswald:wght@300;500;600;700&display=swap" rel="stylesheet">
<style>
  :root{
    --brand-green:#1f6f3c;
    --deep-green:#145a2d;
    --ink:#333333;
    --muted:#4a4a4a;
    --paper:#ffffff;
    --stage:#dcdddf;
    --panel-grey:#ececec;
  }
  *{margin:0;padding:0;box-sizing:border-box}
  html,body{width:1200px;height:764px;overflow:hidden;background:var(--stage)}
  .flyer{position:absolute;left:305px;top:0;width:590px;height:764px;background:var(--paper);overflow:hidden;font-family:"Lato",sans-serif;color:var(--ink)}
  .flyer__lower-panel{position:absolute;left:0;top:440px;width:590px;height:260px;background:linear-gradient(180deg,#ffffff 0%,var(--panel-grey) 100%)}
  .hero{position:absolute;left:0;top:0}
  .brand{position:absolute;left:446px;top:58px;display:flex;align-items:center;gap:7px;color:var(--brand-green);font-family:"Lato",sans-serif;font-weight:700;font-size:13px;line-height:1.2;letter-spacing:.3px}
  .brand__dot{width:22px;height:22px;border-radius:50%;background:var(--brand-green);flex:none}
  .headshot{position:absolute;left:420px;top:258px;width:120px;height:120px;border-radius:50%;border:5px solid var(--brand-green);box-shadow:0 0 0 4px var(--paper);background:radial-gradient(circle at 50% 40%,#c99f86 0%,#8e7a70 45%,#4e5458 100%)}
  .section-title{font-family:"Oswald",sans-serif;font-weight:600;color:var(--brand-green);text-transform:uppercase;letter-spacing:.5px}
  .bio{position:absolute;left:26px;top:290px;width:272px}
  .bio .section-title{font-size:12px;margin-bottom:3px}
  .bio__text{font-size:7.6px;line-height:1.38;color:var(--muted)}
  .headline-rule{position:absolute;left:308px;top:392px;width:1px;height:86px;background:var(--brand-green)}
  .headline{position:absolute;left:320px;top:380px;font-family:"Oswald",sans-serif;line-height:1.05}
  .headline__city{display:block;font-weight:300;font-size:27px;color:var(--brand-green)}
  .headline__line{display:block;font-weight:600;font-size:23px;color:var(--ink);text-transform:uppercase}
  .headline__team{display:block;font-weight:700;font-size:31px;color:var(--brand-green);text-transform:uppercase}
  .clients{position:absolute;left:40px;top:462px;width:240px}
  .clients .section-title{font-size:12px;margin-bottom:6px}
  .bullet-list{list-style:none;font-family:"Oswald",sans-serif;font-weight:500;text-transform:uppercase;color:var(--ink)}
  .bullet-list li{position:relative;padding-left:16px}
  .bullet-list li::before{content:"";position:absolute;left:0;top:.52em;width:6px;height:6px;border-radius:50%;background:var(--brand-green)}
  .clients .bullet-list li{font-size:15px;line-height:19px}
  .column-rule{position:absolute;left:300px;top:545px;width:1px;height:135px;background:#9aa59d}
  .affiliations{position:absolute;left:318px;top:522px;width:250px}
  .affiliations .section-title{font-size:12px;margin-bottom:6px}
  .affiliations .bullet-list li{font-size:14px;line-height:17px;margin-bottom:4px}
  .contact-band{position:absolute;left:0;top:700px;width:590px;height:64px;background:var(--brand-green);color:#ffffff;display:flex;align-items:center;font-size:9px;line-height:1.45}
  .contact-band__item{padding:0 24px}
  .contact-band__item + .contact-band__item{border-left:1px solid rgba(255,255,255,.55)}
  .contact-band__name{font-weight:700}
</style>
</head>
<body>
<main class="flyer">
  <div class="flyer__lower-panel"></div>

  <svg class="hero" width="590" height="400" viewBox="0 0 590 400" xmlns="http://www.w3.org/2000/svg">
    <defs>
      <linearGradient id="scene-tones" x1="0" y1="0" x2="0" y2="1">
        <stop offset="0" stop-color="#9cc7e6"/>
        <stop offset=".55" stop-color="#c9c3a8"/>
        <stop offset="1" stop-color="#5f8f3e"/>
      </linearGradient>
    </defs>
    <path role="img" aria-label="Photo of a real estate agent greeting a smiling couple in front of a house"
          d="M0 0 H405 C440 90 505 165 590 205 V262 C470 282 385 272 300 256 C200 236 90 214 0 222 Z"
          fill="url(#scene-tones)"/>
    <path d="M408 0 C445 92 510 168 590 208" fill="none" stroke="var(--brand-green)" stroke-width="9"/>
    <path d="M0 222 C90 214 200 236 300 256 C385 272 470 282 590 262 V288 C470 304 385 296 300 280 C200 260 95 240 0 246 Z"
          fill="var(--brand-green)"/>
    <path d="M120 246 C200 258 260 272 320 284 C400 300 480 306 590 296" fill="none" stroke="var(--deep-green)" stroke-width="4"/>
  </svg>

  <div class="brand">
    <span class="brand__dot"></span>
    <span>Holbrook Valere<br>Real Estate</span>
  </div>

  <div class="headshot" role="img" aria-label="Portrait photo of the broker"></div>

  <section class="bio">
    <h2 class="section-title">Bio</h2>
    <p class="bio__text">Conrad began his real estate career in 2005 and has completed $75+ million in transactions representing sellers and buyers of commercial real estate, providing tenant representation and leasing of retail and office properties. Prior to beginning his real estate career, Conrad served seven years in the Army Reserves and attended Pinewood Valley College. Conrad has earned the Certified Commercial Realty designation as well as the Retail Leasing Specialist designation. He is a member of the regional council of shopping centers and serves on the board of directors for the local chamber of commerce, the Sandhills youth league and the county arts council. Conrad is a licensed real estate broker in NC and SC.</p>
  </section>

  <div class="headline-rule"></div>
  <h1 class="headline">
    <span class="headline__city">Fayetteville</span>
    <span class="headline__line">Top Retail Leasing &amp;</span>
    <span class="headline__team">Acquistion Team</span>
  </h1>

  <section class="clients">
    <h2 class="section-title">Clients Served</h2>
    <ul class="bullet-list">
      <li>Cluckhouse</li>
      <li>Ten Burgers</li>
      <li>Trim Station</li>
      <li>Tread Depot</li>
      <li>Little Cakery</li>
      <li>Harbor Healthcare</li>
      <li>Kinfolk Services</li>
      <li>Corner Market</li>
      <li>Piedmont Bottling Co.</li>
    </ul>
  </section>

  <div class="column-rule"></div>

  <section class="affiliations">
    <h2 class="section-title">Professional Affiliations</h2>
    <ul class="bullet-list">
      <li>Certified Commercial Realty Member (Designee)</li>
      <li>Regional Council of Retail Centers</li>
      <li>Sandhills Realtors Association</li>
      <li>Carolina Realtors Commercial Forms Committee</li>
    </ul>
  </section>

  <footer class="contact-band">
    <div class="contact-band__item">
      <div class="contact-band__name">T. Conrad Ashby, CCRM, RLS</div>
      <div>Principal / Broker in Charge</div>
    </div>
    <div class="contact-band__item">
      <div>Office Phone: (910) 555-0142 ext. 202</div>
      <div>Cell Phone: (910) 555-0187</div>
    </div>
    <div class="contact-band__item">
      <div>Email: conrad@holbrookvalere.com</div>
      <div>Website: www.holbrookvalere.com</div>
    </div>
  </footer>
</main>
</body>
</html>
```